Consulting firm looking for brochure design

Loring & Vance Consulting is a firm based in Glenharrow looking to update brochure design. We offer a broad range of development expertise to public, private and institutional clients. We would like to see brochure ideas including our company work, the services included, our individual qualifications and a list showing the clients we have served both public and private. We would like brochure to include the colors red, black, gray, and/or white only and to have our logo displayed on brochure pages. Files attached include a PPT with company information we'd like to see included in brochure, company logo designs to choose from to include in brochure, and the previous brochure that we are wanting to replace.
**Note that we are rebranding from " Warren Hollis Economic Development, LLC" to "Loring & Vance Consulting"**
**We have added a total of four logo designs; Two Portrait and Two Landscape both with the options of black backgrounds vs white backgrounds to choose from**

```html
<!DOCTYPE html>
<html lang="en">
<head>
<meta charset="utf-8">
<title>Loring &amp; Vance Consulting Brochure</title>
<link rel="stylesheet" href="https://fonts.googleapis.com/css2?family=Poppins:wght@400;500;600;700;800&display=swap">
<style>
:root{
  --red:#d71f27;
  --red-dark:#8e0d12;
  --black:#111111;
  --ink:#2a2a2a;
  --gray-bg:#c9c9c9;
  --line:#bdbdbd;
  --white:#ffffff;
}
*{margin:0;padding:0;box-sizing:border-box}
html,body{width:914px;height:1200px;overflow:hidden;background:var(--gray-bg);font-family:'Poppins',sans-serif;color:var(--ink)}
.canvas{position:relative;width:914px;height:1200px}
.page{position:absolute;width:375px;height:529px;background:var(--white);box-shadow:0 2px 6px rgba(0,0,0,.25);overflow:hidden}
.page--intro{left:82px;top:67px}
.page--owen{left:469px;top:67px}
.page--claire{left:82px;top:612px}
.page--clients{left:470px;top:612px}
.abs{position:absolute}

/* brand lockup */
.brand{position:absolute;display:flex;align-items:center;gap:6px;color:var(--ink)}
.brand__mark{background:var(--red)}
.brand__name{font-weight:400;line-height:1}
.brand__name small{display:block;text-align:center;letter-spacing:.22em}
.brand--hero{left:0;right:0;top:30px;justify-content:center}
.brand--hero .brand__mark{width:36px;height:36px}
.brand--hero .brand__name{font-size:15px}
.brand--hero .brand__name small{font-size:8.5px;margin-top:3px}
.brand--foot{left:26px;top:484px}
.brand--foot .brand__mark{width:22px;height:22px}
.brand--foot .brand__name{font-size:9.5px}
.brand--foot .brand__name small{font-size:5.6px;margin-top:2px}
.foot-url{position:absolute;right:30px;top:495px;font-size:6.6px;letter-spacing:.08em;font-weight:500}
.foot-rule{position:absolute;left:0;right:0;top:518px;height:2px;background:var(--black)}

/* intro page */
.intro-title{position:absolute;left:0;right:0;top:90px;text-align:center;color:var(--red);font-weight:800;font-size:15.5px}
.intro-text{position:absolute;left:26px;width:323px;top:122px;font-size:7.2px;line-height:13px;text-align:justify;text-align-last:center}
.services{position:absolute;left:26px;top:222px;width:323px;height:147px;border:1px solid var(--line);border-radius:5px}
.services__title{position:absolute;left:50%;top:-11px;transform:translateX(-50%);background:var(--white);padding:0 8px;color:var(--red);font-weight:800;font-size:15px;white-space:nowrap}
.service{position:absolute;display:flex;align-items:center;gap:9px;font-size:7.6px;font-weight:600;line-height:11px;color:var(--ink)}
.service__icon{width:28px;height:28px;border-radius:50%;background:radial-gradient(circle at 35% 30%,var(--red),var(--red-dark));flex:none}
.band{position:absolute;left:0;top:387px;width:375px;height:142px}
.band__title{position:absolute;left:195px;top:13px;color:var(--white);font-weight:700;font-size:10px;white-space:nowrap}
.band__list{position:absolute;top:28px;list-style:none;color:var(--white);font-size:7.6px;line-height:13px}
.band__list li{white-space:nowrap}
.band__url{position:absolute;left:226px;top:120px;color:var(--white);font-weight:600;font-size:8.4px;white-space:nowrap}

/* qualification header */
.qhead__firm{position:absolute;left:25px;top:47px;font-weight:600;font-size:10.6px;color:var(--black);white-space:nowrap}
.qhead__title{position:absolute;left:24px;top:63px;font-weight:800;font-size:18.6px;color:var(--red);white-space:nowrap}
.qhead__bar{position:absolute;left:200px;top:37px;width:3px;height:56px;background:var(--black)}
.qhead__photo{position:absolute;left:206px;top:37px;width:160px;height:56px;border-radius:0 28px 28px 0;background:linear-gradient(110deg,#b3121a,#e0262e 55%,#9c0e14)}

.bio__name{position:absolute;left:26px;top:120px;font-weight:700;font-size:13px;color:var(--black)}
.bio__text{position:absolute;left:26px;width:323px;font-size:7.4px;line-height:13px;text-align:justify}
.bio__text em{font-style:normal;color:var(--red);font-weight:600}

.edu__label{position:absolute;left:18px;top:457px;transform:rotate(-90deg);transform-origin:0 0;width:118px;font-weight:800;font-size:19px;color:var(--red);letter-spacing:.02em}
.edu-card{position:absolute;top:369px;width:127px;height:87px;border:1px solid var(--line);border-radius:5px;text-align:center}
.edu-card__pin{position:absolute;left:50%;top:-26px;transform:translateX(-50%);width:48px;height:56px}
.edu-card__degree{position:absolute;left:0;right:0;color:var(--red);font-weight:700;font-size:10px;line-height:13px}
.edu-card__school{position:absolute;left:0;right:0;font-size:7.4px;font-weight:500;color:var(--black)}

/* clients page */
.clients__tab{position:absolute;top:141px;height:20px;background:var(--red);color:var(--white);font-weight:700;font-size:12px;line-height:20px;padding-left:6px;border-radius:4px 4px 0 0}
.clients__box{position:absolute;top:160px;height:302px;border:1px solid var(--line);border-radius:0 5px 5px 5px}
.clients__list{position:absolute;top:168px;list-style:none;font-size:7.8px;font-weight:600;line-height:14.45px;color:var(--black);white-space:nowrap}
.clients__list li::before{content:"• "}
</style>
</head>
<body>
<div class="canvas">

  <!-- page 1: company overview -->
  <section class="page page--intro">
    <div class="brand brand--hero">
      <span class="brand__mark"></span>
      <span class="brand__name">LORING &amp; VANCE<small>CONSULTING</small></span>
    </div>
    <h1 class="intro-title">LORING &amp; VANCE CONSULTING</h1>
    <p class="intro-text">Loring &amp; Vance Consulting offers a broad range of development expertise to public, private and institutional clients. With strategic guidance, we help navigate public-private partnerships, local government policies, creative incentive financing, project/program management, and many more of the challenges facing our clients. We present an unsurpassed level of quality and commitment by providing sensible solutions that are customized to meet the shifting needs of today’s economy.</p>

    <div class="services">
      <h2 class="services__title">SERVICES INCLUDE</h2>
      <div class="service" style="left:8px;top:31px"><span class="service__icon"></span><span>Public Private<br>Partnership Structuring</span></div>
      <div class="service" style="left:187px;top:31px"><span class="service__icon"></span><span>Chapter 380 Grant<br>Contract Negotiations</span></div>
      <div class="service" style="left:8px;top:67px"><span class="service__icon"></span><span>Incentive<br>Negotiations</span></div>
      <div class="service" style="left:187px;top:67px"><span class="service__icon"></span><span>City Council<br>Workshops</span></div>
      <div class="service" style="left:8px;top:102px"><span class="service__icon"></span><span>Creating and Amending Tax<br>Increment Reinvestments Zones</span></div>
      <div class="service" style="left:187px;top:102px"><span class="service__icon"></span><span>Economic<br>Impact Reporting</span></div>
    </div>

    <div class="band">
      <svg class="abs" width="375" height="142" viewBox="0 0 375 142" style="left:0;top:0">
        <rect x="0" y="0" width="375" height="142" fill="#d71f27" role="img" aria-label="Large brand decoration in red"/>
        <polygon points="163,0 375,0 375,113 212,113" fill="#111111"/>
        <polygon points="212,113 375,113 375,142 222,142" fill="#d71f27"/>
      </svg>
      <div class="band__title">Real Estate Financial Analysis</div>
      <ul class="band__list">
        <li style="margin-left:201px">• Taxable Value Analysis</li>
        <li style="margin-left:206px">• Pro-forma Analysis</li>
        <li style="margin-left:211px">• Underwriting of Incentive Package</li>
        <li style="margin-left:217px">• Market/Financial Feasibility</li>
        <li style="margin-left:222px">• Cost/Benefit Analysis</li>
        <li style="margin-left:228px">• Appraisal review</li>
      </ul>
      <div class="band__url">
        <svg width="7" height="7" viewBox="0 0 10 10" style="vertical-align:-1px;margin-right:3px"><circle cx="5" cy="5" r="4.2" fill="none" stroke="#fff" stroke-width="1"/><ellipse cx="5" cy="5" rx="1.8" ry="4.2" fill="none" stroke="#fff" stroke-width=".8"/><line x1=".8" y1="5" x2="9.2" y2="5" stroke="#fff" stroke-width=".8"/></svg>www.loringvance.com
      </div>
    </div>
  </section>

  <!-- page 2: Owen Loring -->
  <section class="page page--owen">
    <div class="qhead__firm">LORING &amp; VANCE CONSULTING</div>
    <div class="qhead__title">QUALIFICATIONS</div>
    <div class="qhead__bar"></div>
    <div class="qhead__photo" role="img" aria-label="Red-toned photo of office towers"></div>

    <h2 class="bio__name">Owen Loring</h2>
    <p class="bio__text" style="top:147px"><em>With over 30 years of experience</em>, Owen Loring oversees economic development and real estate development projects for Loring &amp; Vance Consulting. Owen focuses on public-private partnerships for medium to large size real estate projects. His efforts include conducting feasibility analysis, contract negotiations and financing mechanisms such as TIF, abatements, and rebates, for both public and private sector clients. Owen’s extensive experience with multifaceted complex projects provides him with unique insight and creative solutions for complex problems. His previous projects include the successful development and redevelopment of The Summit, Eastgate, Granger Plaza, West 9th in Ridgefort, Texas, restructuring Harbor Park in Dalemont, Texas, Arbor Crossing in Arbordale, Texas, and Bayfront Mall in Port Selwyn, Texas. Additionally, he has both managed and created multiple tax increment reinvestment zones and public improvement districts addressing a wide range of issues throughout the state of Texas.</p>

    <div class="edu__label">EDUCATION</div>
    <div class="edu-card" style="left:70px">
      <svg class="edu-card__pin" viewBox="0 0 48 56"><path d="M24 1a23 23 0 0 1 6 45.2L24 55l-6-8.8A23 23 0 0 1 24 1z" fill="#c0141c"/><circle cx="24" cy="24" r="14" fill="#fff"/><rect x="18" y="19" width="12" height="9" rx="1" fill="none" stroke="#111" stroke-width="1.6"/></svg>
      <div class="edu-card__degree" style="top:44px">Master of Public<br>Administration</div>
      <div class="edu-card__school" style="top:70px">North Plains University</div>
    </div>
    <div class="edu-card" style="left:221px">
      <svg class="edu-card__pin" viewBox="0 0 48 56"><path d="M24 1a23 23 0 0 1 6 45.2L24 55l-6-8.8A23 23 0 0 1 24 1z" fill="#c0141c"/><circle cx="24" cy="24" r="14" fill="#fff"/><rect x="18" y="19" width="12" height="9" rx="1" fill="none" stroke="#111" stroke-width="1.6"/></svg>
      <div class="edu-card__degree" style="top:44px">Bachelor of Arts<br>Political Science</div>
      <div class="edu-card__school" style="top:70px">Caprock State University</div>
    </div>

    <div class="brand brand--foot"><span class="brand__mark"></span><span class="brand__name">LORING &amp; VANCE<small>CONSULTING</small></span></div>
    <div class="foot-url">WWW.LORINGVANCE.COM</div>
    <div class="foot-rule"></div>
  </section>

  <!-- page 3: Claire Vance -->
  <section class="page page--claire">
    <div class="qhead__firm">LORING &amp; VANCE CONSULTING</div>
    <div class="qhead__title">QUALIFICATIONS</div>
    <div class="qhead__bar"></div>
    <div class="qhead__photo" role="img" aria-label="Red-toned abstract consulting technology graphic"></div>

    <h2 class="bio__name">Claire Vance</h2>
    <p class="bio__text" style="top:150px">Claire focuses on economic development and real estate development projects and maximizing opportunities for public-private partnerships. Claire is a former Business Development Coordinator for the City of Cedarmere’s Economic Development Department. During her time with the City, her responsibilities included the implementation of incentives, including tax abatements, economic development program grants, tax increment financing, EB-5 funding, and state tax incentives. Prior to joining the City of Cedarmere, Claire was an Analyst with Keystone Realty Advisors in Cedarmere, where her work focused on commercial real estate appraisals used for loan underwriting purposes for a variety of property types, including office, hotel, industrial, retail, and multifamily. Earlier in her career, Claire was an Associate in Meridian’s brokerage services division. In her role, she was responsible for negotiating and executing office and industrial lease and sale transactions.</p>

    <div class="edu__label">EDUCATION</div>
    <div class="edu-card" style="left:70px">
      <svg class="edu-card__pin" viewBox="0 0 48 56"><path d="M24 1a23 23 0 0 1 6 45.2L24 55l-6-8.8A23 23 0 0 1 24 1z" fill="#c0141c"/><circle cx="24" cy="24" r="14" fill="#fff"/><rect x="18" y="19" width="12" height="9" rx="1" fill="none" stroke="#111" stroke-width="1.6"/></svg>
      <div class="edu-card__degree" style="top:32px">Master of Business<br>Administration<br>Corporate Finance</div>
      <div class="edu-card__school" style="top:71px">Trinity River University</div>
    </div>
    <div class="edu-card" style="left:221px">
      <svg class="edu-card__pin" viewBox="0 0 48 56"><path d="M24 1a23 23 0 0 1 6 45.2L24 55l-6-8.8A23 23 0 0 1 24 1z" fill="#c0141c"/><circle cx="24" cy="24" r="14" fill="#fff"/><rect x="18" y="19" width="12" height="9" rx="1" fill="none" stroke="#111" stroke-width="1.6"/></svg>
      <div class="edu-card__degree" style="top:38px">BBA<br>Management</div>
      <div class="edu-card__school" style="top:67px">Brazos Valley University</div>
    </div>

    <div class="brand brand--foot"><span class="brand__mark"></span><span class="brand__name">LORING &amp; VANCE<small>CONSULTING</small></span></div>
    <div class="foot-url">WWW.LORINGVANCE.COM</div>
    <div class="foot-rule"></div>
  </section>

  <!-- page 4: clients -->
  <section class="page page--clients">
    <div class="qhead__firm">LORING &amp; VANCE CONSULTING</div>
    <div class="qhead__title">QUALIFICATIONS</div>
    <div class="qhead__bar"></div>
    <div class="qhead__photo" role="img" aria-label="Red-toned photo of a business meeting"></div>

    <div class="clients__tab" style="left:27px;width:99px">Public Clients</div>
    <div class="clients__box" style="left:27px;width:151px"></div>
    <ul class="clients__list" style="left:33px">
      <li>Amberfield</li><li>Ashcombe</li><li>Alderwick</li><li>Bayhollow</li><li>Cedarmere</li><li>Copperleaf</li><li>Cresthaven</li><li>Dunmorrow</li><li>Elkbend</li><li>Fenwold</li><li>Foxmere</li><li>Glenharrow</li><li>Harrowby</li><li>Hollowmere</li><li>Ironbend</li><li>Kestrel Point</li><li>Larkmoor</li><li>Marrowfield</li><li>Quillby</li><li>Wrenford</li>
    </ul>

    <div class="clients__tab" style="left:197px;width:104px">Private Clients</div>
    <div class="clients__box" style="left:197px;width:152px"></div>
    <ul class="clients__list" style="left:202px">
      <li>Hearthstone Communities</li><li>Alderleaf Homes</li><li>Bastion Frontier</li><li>Crestmark Real Estate</li><li>Silverpine Equities</li><li>Finch &amp; Lowe Developments</li><li>Halvorsen</li><li>Quarry Global</li><li>Jessup Marlow</li><li>Kettleby Realty</li><li>Lantern Commercial</li><li>Regalia Realty</li><li>Morrow Interest</li><li>Orrin Developments</li><li>Northvale Properties</li><li>QRT</li><li>Rowan Glenmark</li><li>Saltmarsh Outlets</li><li>Tidewell</li><li>Unity Bridge Development</li>
    </ul>

    <div class="brand brand--foot"><span class="brand__mark"></span><span class="brand__name">LORING &amp; VANCE<small>CONSULTING</small></span></div>
    <div class="foot-url">WWW.LORINGVANCE.COM</div>
    <div class="foot-rule"></div>
  </section>

</div>
</body>
</html>
```